Business Card Design Project

We are an agricultural business based in Brisbane.
We design, manage and operate regional saleyards. Our logo is green/silver in colour and details of our business can be found on our website www.tovrak.com.au

Just wanting a corporate design for some business cards and include name, position, contact details.

Thanks

```html
<!DOCTYPE html>
<html lang="en">
<head>
<meta charset="utf-8">
<title>Tovrak Business Card</title>
<link href="https://fonts.googleapis.com/css2?family=PT+Sans+Narrow:wght@700&family=Arimo:wght@400&display=swap" rel="stylesheet">
<style>
  :root {
    --backdrop: #3a3a3a;
    --card-white: #ffffff;
    --brand-green: #00873e;
    --ink: #231f20;
    --on-green: #ffffff;
  }
  html, body {
    margin: 0;
    width: 1200px;
    height: 797px;
    overflow: hidden;
    background: var(--backdrop);
  }
  .business-card {
    position: absolute;
    left: 250px;
    top: 198px;
    width: 700px;
    height: 400px;
    background: var(--card-white);
    box-shadow: 0 6px 18px rgba(0,0,0,0.45);
    overflow: hidden;
  }
  .holder {
    position: absolute;
    left: 18px;
    top: 14px;
  }
  .holder-name {
    margin: 0;
    font-family: "PT Sans Narrow", sans-serif;
    font-weight: 700;
    font-size: 36px;
    line-height: 1.05;
    color: var(--ink);
  }
  .holder-role {
    margin: 0;
    font-family: "Arimo", sans-serif;
    font-size: 22px;
    line-height: 1.2;
    color: var(--brand-green);
  }
  .company-name {
    position: absolute;
    left: 0;
    right: 0;
    top: 108px;
    display: flex;
    justify-content: center;
    align-items: center;
    gap: 18px;
  }
  .company-mark {
    width: 34px;
    height: 34px;
    background: var(--brand-green);
  }
  .company-word {
    font-family: "PT Sans Narrow", sans-serif;
    font-weight: 700;
    font-size: 72px;
    letter-spacing: 2px;
    color: var(--ink);
    text-transform: uppercase;
  }
  .contact-band {
    position: absolute;
    left: 0;
    right: 0;
    bottom: 0;
    height: 96px;
    background: var(--brand-green);
    display: flex;
    justify-content: center;
    align-items: flex-end;
    gap: 32px;
    padding-bottom: 18px;
    box-sizing: border-box;
  }
  .contact-item {
    display: flex;
    align-items: center;
    gap: 6px;
    font-family: "Arimo", sans-serif;
    font-size: 19px;
    color: var(--on-green);
  }
  .contact-icon {
    width: 26px;
    height: 24px;
    fill: none;
    stroke: var(--on-green);
    stroke-width: 1.6;
  }
</style>
</head>
<body>
  <div class="business-card">
    <div class="holder">
      <p class="holder-name">Dean Whitford</p>
      <p class="holder-role">Managing Director</p>
    </div>

    <div class="company-name">
      <span class="company-mark"></span>
      <span class="company-word">Tovrak</span>
    </div>

    <div class="contact-band">
      <span class="contact-item">
        <svg class="contact-icon" viewBox="0 0 26 24" aria-hidden="true">
          <rect x="2" y="5" width="22" height="15"/>
          <path d="M2 5 L13 14 L24 5"/>
        </svg>
        dean@tovrak.com.au
      </span>
      <span class="contact-item">
        <svg class="contact-icon" viewBox="0 0 26 24" aria-hidden="true">
          <circle cx="13" cy="12" r="10.5"/>
          <path d="M9 6 q-2 6 4 12 l3 -2 l-2 -3 l-2 1 q-2 -3 -1 -5 l2 -1 l-1 -3 z"/>
        </svg>
        0400 123 987
      </span>
      <span class="contact-item">
        <svg class="contact-icon" viewBox="0 0 26 24" aria-hidden="true">
          <ellipse cx="13" cy="12" rx="11" ry="8"/>
          <path d="M2 12 h22 M13 4 v16"/>
        </svg>
        www.tovrak.com.au
      </span>
    </div>
  </div>
</body>
</html>
```